Varneck Bidding Business Cards Design Needed

I need a business card design that is modern looking - double sided (maybe just my logo on the back, but open to suggestions) - the overall design is up to you. I want it to be easy to read - not over the top flashy. I already have a company logo which I uploaded so that needs to be used. The colors of my logo are the colors I want on the card... so blue and gray (do need to match the logo colors).

Requirements
Must have
• Would like the card to be sleek, modern and easy to ready

```html
<!DOCTYPE html>
<html lang="en">
<head>
<meta charset="utf-8">
<title>Varneck Bidding – Business Cards</title>
<link href="https://fonts.googleapis.com/css2?family=Ubuntu:wght@400;500;700&display=swap" rel="stylesheet">
<style>
  :root {
    --blue: #2f7fc1;
    --blue-light: #4a97cf;
    --blue-dark: #2a6fab;
    --gray: #6a6d72;
    --gray-dark: #4b4e53;
    --paper: #f4f4f4;
    --paper-edge: #e6e6e6;
    --stage: #d9dcdf;
  }
  * { box-sizing: border-box; margin: 0; padding: 0; }
  html, body {
    width: 1200px; height: 900px; overflow: hidden;
    background: var(--stage);
    font-family: "Ubuntu", sans-serif;
  }
  .stage {
    width: 1200px; height: 900px;
    display: flex; flex-direction: column;
    align-items: center; justify-content: center; gap: 48px;
  }
  .card {
    width: 620px; height: 354px; position: relative;
    border-radius: 2px;
    box-shadow: 0 10px 24px rgba(0,0,0,.18);
    overflow: hidden;
  }
  /* back side */
  .card-back {
    background: linear-gradient(160deg, var(--blue-dark) 0%, var(--blue-light) 100%);
    display: flex; align-items: center; justify-content: center;
  }
  .card-back .brand {
    color: #fff; font-weight: 700; font-size: 40px; letter-spacing: 2px;
    text-transform: uppercase; display: flex; align-items: center; gap: 14px;
  }
  .brand-dot { width: 16px; height: 16px; background: currentColor; border-radius: 50%; }
  /* front side */
  .card-front {
    background: linear-gradient(135deg, #fbfbfb 0%, var(--paper) 60%, var(--paper-edge) 100%);
  }
  .card-front .brand {
    position: absolute; left: 40px; top: 40px;
    color: var(--blue); font-weight: 700; font-size: 26px; letter-spacing: 1.5px;
    text-transform: uppercase;
  }
  .side-band {
    position: absolute; right: 34px; top: 0; width: 9px; height: 300px;
    background: var(--blue);
  }
  .tagline {
    position: absolute; right: 52px; top: 10px;
    writing-mode: vertical-rl;
    font-size: 14px; color: var(--gray-dark); letter-spacing: .5px;
  }
  .person { position: absolute; left: 40px; top: 170px; }
  .person-name { color: var(--blue); font-weight: 700; font-size: 30px; }
  .person-role { color: var(--gray); font-size: 16px; margin-top: 2px; }
  .contact { position: absolute; left: 40px; top: 250px; list-style: none; }
  .contact li {
    display: flex; align-items: center; gap: 10px;
    color: var(--gray-dark); font-size: 17px; line-height: 26px;
  }
  .contact svg { width: 15px; height: 15px; flex: none; }
</style>
</head>
<body>
<main class="stage">
  <section class="card card-back" aria-label="Card back">
    <div class="brand"><span class="brand-dot"></span>Varneck Bidding</div>
  </section>

  <section class="card card-front" aria-label="Card front">
    <div class="brand">Varneck Bidding</div>
    <div class="side-band"></div>
    <p class="tagline">Improving Charity Auctions Nationwide</p>

    <div class="person">
      <h1 class="person-name">Marcus Hale</h1>
      <p class="person-role">Owner/President - Auctioneer</p>
    </div>

    <ul class="contact">
      <li>
        <svg viewBox="0 0 16 16" aria-hidden="true"><path fill="#2f7fc1" d="M3.5 1.5l2.5 3-1.5 1.5c.8 2 2.5 3.7 4.5 4.5L10.5 9l3 2.5-1.5 2.5C7 14 2 9 1.5 3z"/></svg>
        555-014-7290
      </li>
      <li>
        <svg viewBox="0 0 16 16" aria-hidden="true"><rect x="1" y="3" width="14" height="10" fill="none" stroke="#2f7fc1" stroke-width="1.6"/><path d="M1 3l7 6 7-6" fill="none" stroke="#2f7fc1" stroke-width="1.6"/></svg>
        hello@varneckbidding.com
      </li>
      <li>
        <svg viewBox="0 0 16 16" aria-hidden="true"><g fill="none" stroke="#2f7fc1" stroke-width="1.3"><circle cx="8" cy="8" r="6.5"/><ellipse cx="8" cy="8" rx="3" ry="6.5"/><path d="M1.5 8h13M2.5 4.8h11M2.5 11.2h11"/></g></svg>
        www.varneckbidding.com
      </li>
    </ul>
  </section>
</main>
</body>
</html>
```